Marrowgate Auctions Business Cards Design Needed

I need a business card design that is modern looking - double sided (maybe just my logo on the back, but open to suggestions) - the overall design is up to you. I want it to be easy to read - not over the top flashy. I already have a company logo which I uploaded so that needs to be used. The colors of my logo are the colors I want on the card... so blue and gray (do need to match the logo colors).

Requirements
Must have
• Would like the card to be sleek, modern and easy to ready

```html
<!DOCTYPE html>
<html lang="en">
<head>
<meta charset="utf-8">
<title>Marrowgate Auctions Business Cards</title>
<link rel="stylesheet" href="https://fonts.googleapis.com/css2?family=Saira:wght@400;600&family=Lato:wght@400&display=swap">
<style>
  :root {
    --backdrop: #2a2a2a;
    --card-white: #ffffff;
    --brand-blue: #2d7bc4;
    --brand-blue-light: #3a86cc;
    --brand-gray: #555759;
    --text-dark: #222222;
    --rule-gray: #9a9a9a;
  }
  * { margin: 0; padding: 0; box-sizing: border-box; }
  html, body { width: 1200px; height: 1200px; overflow: hidden; }
  body { background: var(--backdrop); position: relative; }

  .card {
    position: absolute;
    top: 310px;
    width: 366px;
    height: 594px;
    box-shadow: 0 4px 10px rgba(0,0,0,0.5);
  }
  .card--front { left: 234px; background: var(--card-white); }
  .card--back  { left: 628px; width: 368px; background: var(--brand-blue); }

  .brand {
    position: absolute;
    top: 118px;
    left: 0; right: 0;
    text-align: center;
  }
  .brand__dot {
    display: block;
    width: 56px; height: 56px;
    margin: 0 auto 18px;
    border-radius: 50%;
    background: var(--brand-blue);
  }
  .brand__name {
    font-family: "Saira", sans-serif;
    font-weight: 600;
    font-size: 30px;
    line-height: 1.05;
    letter-spacing: 0.5px;
    color: var(--brand-gray);
  }

  .contact {
    position: absolute;
    top: 384px;
    left: 0; right: 0;
    text-align: center;
  }
  .contact__name {
    font-family: "Saira", sans-serif;
    font-weight: 400;
    font-size: 24px;
    letter-spacing: 0.5px;
    line-height: 1;
    color: var(--brand-gray);
  }
  .contact__name .first { color: var(--brand-blue); }
  .contact__role {
    font-family: "Lato", sans-serif;
    font-size: 17px;
    color: var(--text-dark);
    margin-top: 6px;
  }
  .contact__icons {
    display: flex;
    align-items: center;
    justify-content: center;
    gap: 4px;
    margin-top: 18px;
  }
  .contact__rule { width: 54px; height: 1px; background: var(--rule-gray); margin: 0 1px; }
  .contact__lines {
    font-family: "Lato", sans-serif;
    font-size: 17px;
    line-height: 22px;
    color: var(--text-dark);
    margin-top: 10px;
  }

  .back__title {
    position: absolute;
    top: 444px;
    left: 0; right: 0;
    text-align: center;
    font-family: "Saira", sans-serif;
    font-weight: 600;
    font-size: 27px;
    letter-spacing: 0.3px;
    color: var(--card-white);
  }
  .back__tagline {
    position: absolute;
    top: 502px;
    left: 0; right: 0;
    text-align: center;
    font-family: "Saira", sans-serif;
    font-weight: 400;
    font-size: 18px;
    line-height: 24px;
    color: var(--card-white);
  }
</style>
</head>
<body>

<section class="card card--front">
  <div class="brand">
    <span class="brand__dot"></span>
    <p class="brand__name">MARROWGATE<br>AUCTIONS</p>
  </div>

  <div class="contact">
    <p class="contact__name"><span class="first">NORA</span> LINDQVIST</p>
    <p class="contact__role">Owner/President - Auctioneer</p>
    <div class="contact__icons">
      <span class="contact__rule"></span>
      <svg width="24" height="24" viewBox="0 0 24 24" aria-label="Phone">
        <circle cx="12" cy="12" r="12" fill="#2d7bc4"/>
        <path d="M7 10c0-2 2-3 5-3s5 1 5 3l-2 .5-.5-1.5h-5l-.5 1.5zM8.5 12h7l1 5h-9z" fill="#fff"/>
      </svg>
      <svg width="24" height="24" viewBox="0 0 24 24" aria-label="Email">
        <circle cx="12" cy="12" r="12" fill="#2d7bc4"/>
        <rect x="6.5" y="8" width="11" height="8" fill="#fff"/>
        <path d="M6.5 8l5.5 4.5L17.5 8" fill="none" stroke="#2d7bc4" stroke-width="1.2"/>
      </svg>
      <svg width="24" height="24" viewBox="0 0 24 24" aria-label="Website">
        <circle cx="12" cy="12" r="12" fill="#2d7bc4"/>
        <circle cx="12" cy="12" r="6" fill="none" stroke="#fff" stroke-width="1.4"/>
        <path d="M6 12h12M12 6c-2.5 3-2.5 9 0 12M12 6c2.5 3 2.5 9 0 12" fill="none" stroke="#fff" stroke-width="1"/>
      </svg>
      <span class="contact__rule"></span>
    </div>
    <p class="contact__lines">555-214-3870<br>hello@marrowgateauctions.com<br>www.marrowgatebids.com</p>
  </div>
</section>

<section class="card card--back">
  <p class="back__title">MARROWGATE AUCTIONS</p>
  <p class="back__tagline">IMPROVING CHARITY AUCTIONS<br>NATIONWIDE</p>
</section>

</body>
</html>
```